Pipeline management & construction company needs nice brochure

Red Mesa Engineering & Construction, LLC (www.redmesaec.example) is a company focused on the midstream oil and gas / pipeline business. We plan, route, design, manage, and construction pipelines and related facilities. We need a brochure to summarize our services as well as give a brief listing of projects completed/desired.

Industry/Entity Type

Construction

Font styles to use
Serif

```html
<!DOCTYPE html>
<html lang="en">
<head>
<meta charset="utf-8">
<title>Red Mesa Engineering &amp; Construction, LLC — Brochure</title>
<link href="https://fonts.googleapis.com/css2?family=Montserrat:wght@600;700;800&family=Open+Sans:wght@400;600&display=swap" rel="stylesheet">
<style>
:root{
  --navy:#141a4a;
  --navy-deep:#0b0f2e;
  --ink:#0d0d14;
  --yellow:#f9cf2f;
  --yellow-deep:#f0b90f;
  --white:#ffffff;
  --text:#1d1d1d;
  --page:#e9e9ec;
}
*{box-sizing:border-box;margin:0;padding:0}
html,body{width:1200px;height:811px;overflow:hidden;background:var(--page)}
.brochure{position:relative;width:1200px;height:811px;background:var(--yellow);font-family:"Open Sans",Arial,sans-serif;color:var(--text);overflow:hidden}
.hero{position:absolute;left:0;top:0;width:1200px;height:480px;
  background:linear-gradient(160deg,#1d2a78 0%,#141a4a 45%,#2a3a7a 70%,#0b0f2e 100%)}
.hero::after{content:"";position:absolute;inset:0;background:radial-gradient(ellipse at 45% 70%,rgba(120,150,210,.35),transparent 60%)}
.services{position:absolute;left:40px;top:64px;width:296px;height:390px;background:var(--ink);border-radius:14px;padding:58px 18px 16px;z-index:2}
.services-title{position:absolute;left:0;top:0;width:100%;height:44px;background:var(--yellow);border-radius:14px 14px 0 0;font:800 17px "Montserrat",sans-serif;letter-spacing:1px;text-align:center;line-height:46px;color:var(--ink)}
.service-group{margin-bottom:9px}
.service-head{font:700 11px "Montserrat",sans-serif;color:var(--yellow);text-transform:uppercase;white-space:nowrap}
.service-head::before{content:"➤ ";font-size:10px}
.service-item{color:var(--white);font-size:12px;line-height:1.34;padding-left:4px}
.service-item::before{content:"· "}
.feature{position:absolute;left:355px;width:245px;height:76px;background:var(--yellow);border-radius:8px;display:flex;align-items:center;gap:14px;padding:0 16px;z-index:2;box-shadow:0 3px 8px rgba(0,0,0,.35)}
.feature::after{content:"";position:absolute;right:-14px;top:24px;border-left:14px solid var(--yellow);border-top:14px solid transparent;border-bottom:14px solid transparent}
.feature svg{flex:none;width:40px;height:40px}
.feature-text{font:800 15px/1.2 "Montserrat",sans-serif;color:var(--ink)}
.special{position:absolute;left:630px;top:34px;width:535px;height:356px;background:var(--white);border:6px solid var(--yellow-deep);padding:12px 20px;z-index:2}
.special-title{font:800 15px "Montserrat",sans-serif;color:var(--yellow-deep);text-align:right;margin-bottom:8px}
.special p{font-size:10.5px;line-height:1.38;text-align:justify;text-indent:18px;margin-bottom:8px}
.special p:last-child{margin-bottom:0}
.tagline{position:absolute;left:390px;top:400px;font:800 33px "Montserrat",sans-serif;color:var(--white);z-index:2;letter-spacing:.3px;white-space:nowrap}
.quote-mark{color:var(--white);font-size:42px;vertical-align:-6px}
.projects{position:absolute;left:40px;top:505px;width:1120px;height:270px;background:var(--white);padding:46px 26px 16px;display:flex;gap:30px}
.projects-title{position:absolute;left:0;top:-30px;height:58px;width:310px;background:var(--ink);border-radius:0 14px 0 0;font:800 17px "Montserrat",sans-serif;color:var(--yellow);line-height:58px;padding-left:34px;letter-spacing:.5px}
.project-list{list-style:none;flex:1}
.project-list li{font-size:12.5px;line-height:1.4;margin-bottom:4px;padding-left:14px;position:relative}
.project-list li::before{content:"";position:absolute;left:0;top:6px;width:7px;height:7px;background:var(--yellow)}
</style>
</head>
<body>
<main class="brochure">
  <div class="hero" role="img" aria-label="Photograph of an industrial pipeline corridor with elevated steel pipes under a blue sky"></div>

  <section class="services">
    <h2 class="services-title">SERVICES</h2>
    <div class="service-group">
      <div class="service-head">Project Management</div>
      <div class="service-item">Project Management Consulting</div>
      <div class="service-item">"Cradle to Grave" Project Management</div>
      <div class="service-item">AFE/Budget Preparation</div>
      <div class="service-item">Detailed Design</div>
    </div>
    <div class="service-group">
      <div class="service-head">Construction Management</div>
      <div class="service-item">Route Selection</div>
      <div class="service-item">ROW Acquisition</div>
      <div class="service-item">Survey Coordination</div>
      <div class="service-item">Constructability Reviews</div>
      <div class="service-item">QA/QC Inspection</div>
    </div>
    <div class="service-group"><div class="service-head">LSTK / EPC Projects</div></div>
    <div class="service-group">
      <div class="service-head">Integrity Work</div>
      <div class="service-item">ILI Make Ready Assistance</div>
      <div class="service-item">Anomaly Repair</div>
    </div>
    <div class="service-group"><div class="service-head">Pipeline &amp; Facilities Construction</div></div>
  </section>

  <div class="feature" style="top:82px">
    <svg viewBox="0 0 40 40" aria-hidden="true"><circle cx="20" cy="20" r="11" fill="none" stroke="#0d0d14" stroke-width="6" stroke-dasharray="5 3.6"/><circle cx="20" cy="20" r="9" fill="none" stroke="#0d0d14" stroke-width="3"/><circle cx="20" cy="20" r="3" fill="#0d0d14"/></svg>
    <span class="feature-text">Several services under one banner</span>
  </div>
  <div class="feature" style="top:182px">
    <svg viewBox="0 0 40 40" aria-hidden="true"><circle cx="19" cy="21" r="15" fill="none" stroke="#0d0d14" stroke-width="3"/><circle cx="19" cy="21" r="9" fill="none" stroke="#0d0d14" stroke-width="3"/><circle cx="19" cy="21" r="3" fill="#0d0d14"/><path d="M19 21 L36 4 M30 4h6v6" stroke="#0d0d14" stroke-width="3" fill="none"/></svg>
    <span class="feature-text">Precision in construction planning</span>
  </div>
  <div class="feature" style="top:282px">
    <svg viewBox="0 0 40 40" aria-hidden="true" fill="#0d0d14"><circle cx="20" cy="13" r="5"/><path d="M11 30a9 9 0 0 1 18 0z"/><circle cx="8" cy="17" r="4"/><path d="M1 31a7 7 0 0 1 12-5v5z"/><circle cx="32" cy="17" r="4"/><path d="M39 31a7 7 0 0 0-12-5v5z"/></svg>
    <span class="feature-text">Team of construction focused professionals</span>
  </div>

  <section class="special">
    <h2 class="special-title">WHAT MAKES US SPECIAL...</h2>
    <p>Our services include project management, design, construction, construction management, and Lump Sum-Turn Key/EPC projects. By offering all of these services under one banner we feel we can react quickly to the needs of our customers, which is a must in the current market with so many private equity firms and large companies chasing the new hot beds of activity.</p>
    <p>We plan the work with the construction in mind. It sounds cliché but "plan your work and work your plan" is appropriate when it comes to pipeline and facilities projects. RMEC is of the belief that every minute of proper planning can save valuable time and capital dollars. One too many HDDs, a fitting in the wrong location, or forgetting to consider elevation changes when planning a hydrotest can greatly impact the outcome of a project.</p>
    <p>We plan to direct the design efforts toward streamlining the field construction. Construction is typically the largest portion of most AFE budgets, but sadly it is usually an afterthought, with little attention given to constructability, contract language and unit pricing methodology, or how to select the ideal construction contractor for the type of project being designed. With that in mind, we feel that if the proper attention is given to that area early on in the planning process, then we can save our customers unnecessary headaches and wasted dollars once construction is underway.</p>
  </section>

  <p class="tagline"><span class="quote-mark">“</span> Let Our Experience Work for You... <span class="quote-mark">”</span></p>

  <section class="projects">
    <h2 class="projects-title">OUR LATEST PROJECTS</h2>
    <ul class="project-list">
      <li>Routing, Survey &amp; ROW Acquisition Coordination for the installation of 6 miles of 12" through congested pipeline corridor near Corpus Christi, Texas (2014-15).</li>
      <li>Routing, Survey &amp; ROW Acquisition Coordination for the installation of 60 miles of 12" pipeline in South Texas (2014).</li>
      <li>Preliminary routing and AFE budget preparation for 540 miles of pipeline across Colorado, Kansas, and Oklahoma (2014).</li>
      <li>Constructibility review and routing for a 255 mile pipeline from Midland to Wichita Falls, Texas (2014).</li>
      <li>Routing, Survey &amp; ROW Acquisition Coordination for the installation of 4 miles of 20" and 6" pipeline in Eastern Ohio (2013-14).</li>
    </ul>
    <ul class="project-list">
      <li>Provide Construction Management and Inspection for the installation of 30 miles of 12" pipeline through congested corridors near Houston, Texas (2014-15).</li>
      <li>Safety inspection for the installation of 58 miles of 12" pipeline in South Texas (2014).</li>
      <li>Design and Installation of approximately 4,000 feet of 8" pipeline through "Refinery Row" near Corpus Christi. Project included three (3) complex 8" HDDs (2014-15).</li>
      <li>Construction of 430 miles of 16" NGL pipeline for Keystone Midstream Partners (2013-14).</li>
      <li>Construction of 340 miles of the Plainsway 20" pipeline for Keystone Midstream Partners (2012-13).</li>
      <li>Construction of 562 miles of the 30" Gulfway pipeline for Keystone Midstream Partners (2012-13).</li>
    </ul>
  </section>
</main>
</body>
</html>
```